Bramfield Animal Hospital brochure

We have found that our current clients do not know all of the services that we offer so we want to make a hospital brochure to make our services more known. Our website has all of our services listed but we find that clients aren't looking at our website as much as we would like so we are hoping a hospital brochure can sum up our main services and maybe lead to more people visiting our website. Our hospital colors are blue and maroon and our moto is "Outstanding Medicine, Extraordinary Service." Some of the service we would like to promote more include digital x-ray, ultrasounds, echocardiograms, laser therapy and dentals. We also offer after hours emergency care but only to our current clients. You can find more services listed on our website We are in a small town so we want a personal yet professional feel.

Feel free to visit our website to get a better feel for our business https://thecorvelpets.com/

• 6-8 panel brochure
• I included some photos from around the hospital. If you feel that you can make a few work in the brochure then great but don't feel obligated to.

```html
<!DOCTYPE html>
<html lang="en">
<head>
<meta charset="utf-8">
<title>Bramfield Animal Hospital Brochure</title>
<link rel="stylesheet" href="https://fonts.googleapis.com/css2?family=Arimo:wght@400;700&family=Tinos:wght@400;700&family=Cinzel:wght@500&display=swap">
<style>
  :root {
    --stage: #d9d9d9;
    --white: #ffffff;
    --ink: #1f1f1f;
    --red: #b3131b;
    --maroon: #8e1b24;
    --navy: #1f2a6b;
    --black: #141414;
    --mist: #ececec;
    --yellow: #f2c81c;
  }
  * { box-sizing: border-box; margin: 0; padding: 0; }
  html, body { width: 1200px; height: 800px; overflow: hidden; }
  body { background: var(--stage); position: relative; }

  .brochure { position: absolute; left: 60px; top: 90px; width: 1080px; height: 620px; display: flex; box-shadow: 0 16px 34px rgba(0,0,0,.22); }
  .panel { position: relative; width: 360px; height: 620px; overflow: hidden; }

  /* Emergency panel */
  .panel--emergency { background: var(--white); font-family: "Arimo", Arial, sans-serif; color: var(--ink); }
  .emergency__title { color: var(--red); font-weight: 400; font-size: 25px; line-height: 1.05; text-align: center; margin-top: 30px; letter-spacing: .5px; }
  .emergency__lead { font-size: 11.5px; line-height: 1.45; text-align: center; padding: 14px 30px 0; }
  .emergency__clinic { font-size: 11.5px; text-align: center; margin-top: 12px; }
  .emergency__photos { position: absolute; left: 32px; top: 250px; width: 296px; height: 130px; }
  .photo { position: absolute; }
  .photo--staff-cat { left: 0; top: 14px; width: 130px; height: 110px; background: linear-gradient(160deg, #c9c2b6, #3a4058); }
  .photo--exam-top { left: 142px; top: 0; width: 150px; height: 60px; background: linear-gradient(160deg, #9aa2b1, #3c4a74); }
  .photo--exam-bottom { left: 142px; top: 66px; width: 150px; height: 60px; background: linear-gradient(160deg, #b7b3aa, #2e3a66); }
  .emergency__about { position: absolute; left: 26px; right: 26px; top: 395px; font-size: 11.5px; line-height: 1.45; text-align: center; }
  .emergency__footer { position: absolute; left: 0; bottom: 0; width: 360px; height: 110px; }
  .photo--pets-peek { position: absolute; left: 40px; bottom: 14px; width: 220px; height: 70px; background: linear-gradient(90deg, #2a2a2a, #8a6a4f 55%, #e7d9c6); border-radius: 40px 40px 0 0; }

  /* Contact panel */
  .panel--contact { background: var(--black); color: var(--white); font-family: "Tinos", "Times New Roman", serif; text-align: center; }
  .contact__intro { font-size: 14px; line-height: 1.3; margin-top: 24px; }
  .contact__address { font-weight: 700; font-size: 14px; line-height: 1.3; margin-top: 14px; padding: 0 40px; }
  .contact__lines { list-style: none; font-size: 12.5px; line-height: 1.55; margin-top: 14px; display: inline-block; text-align: left; }
  .contact__lines li { display: flex; align-items: center; gap: 8px; }
  .contact__lines svg { width: 12px; height: 12px; fill: var(--white); }
  .hours__title { font-weight: 700; font-size: 15px; margin-top: 22px; letter-spacing: .5px; }
  .hours__list { list-style: none; font-size: 13.5px; line-height: 1.35; margin-top: 8px; }
  .photo--dog { position: absolute; left: 30px; bottom: 0; width: 190px; height: 160px; background: radial-gradient(ellipse at 50% 60%, #6a6a6a, #1a1a1a 70%); border-radius: 50% 50% 0 0; }
  .contact__marks { position: absolute; right: 22px; bottom: 22px; width: 96px; display: flex; flex-direction: column; align-items: center; gap: 10px; }
  .brand-name--small { font-family: "Tinos", "Times New Roman", serif; color: var(--maroon); font-size: 12px; font-weight: 700; line-height: 1.1; background: var(--white); padding: 6px 4px; border-radius: 4px; width: 96px; }
  .badge { width: 74px; height: 28px; border-radius: 4px; background: var(--white); }
  .badge--tall { height: 40px; width: 40px; }

  /* Cover panel */
  .panel--cover { background: var(--mist); font-family: "Tinos", "Times New Roman", serif; }
  .cover__brand { position: absolute; top: 26px; left: 0; width: 100%; display: flex; justify-content: center; align-items: center; gap: 10px; }
  .cover__brand-square { width: 34px; height: 34px; background: var(--red); }
  .brand-name { color: var(--maroon); font-weight: 700; font-size: 16px; line-height: 1.05; }
  .cover__hero { position: absolute; left: 40px; top: 100px; width: 280px; height: 280px; }
  .cover__title { position: absolute; top: 420px; left: 0; width: 100%; text-align: center; font-family: "Cinzel", "Times New Roman", serif; font-weight: 500; font-size: 21px; line-height: 1.08; color: var(--maroon); }
  .cover__band { position: absolute; left: 0; bottom: 0; width: 100%; height: 70px; }
  .cover__url { position: absolute; left: 0; bottom: 24px; width: 100%; text-align: center; font-size: 13px; color: var(--navy); letter-spacing: .4px; }
</style>
</head>
<body>
<main class="brochure">

  <section class="panel panel--emergency">
    <h2 class="emergency__title">24 HOUR<br>EMERGENCY CARE</h2>
    <p class="emergency__lead">Because minutes can matter. We keep a veterinarian on call 24 hours a day for emergency services. In order to treat your pet as quickly as possible, we restrict after hours emergency care to current clients. If you are not a current client and may be experiencing an after hours pet emergency, please contact your regular veterinarian or Northvale Animal</p>
    <p class="emergency__clinic">Emergency Clinic at (518) 555-0193.</p>
    <div class="emergency__photos">
      <div class="photo photo--staff-cat" role="img" aria-label="Staff member holding a cat in the hospital"></div>
      <div class="photo photo--exam-top" role="img" aria-label="Technician examining a pet on a table"></div>
      <div class="photo photo--exam-bottom" role="img" aria-label="Veterinary team member at the exam table"></div>
    </div>
    <p class="emergency__about">We built Bramfield Animal Hospital for you. It is so important to us that you can walk into an environment where you feel you are always put first, and where the little things have been thought of to make this a truly wonderful experience. We want to make your life easier. We offer evening hours, drop-offs, and house call appointments. And existing clients get access to 24 hour emergency care. Because we are always looking out for you</p>
    <svg class="emergency__footer" viewBox="0 0 360 110" aria-hidden="true">
      <polygon points="0,30 20,30 20,95 360,110 0,110" fill="var(--navy)"/>
      <circle cx="36" cy="42" r="18" fill="var(--yellow)"/>
      <circle cx="318" cy="18" r="9" fill="var(--navy)"/>
    </svg>
    <div class="photo--pets-peek" role="img" aria-label="A cat and a dog peeking up from the bottom edge"></div>
  </section>

  <section class="panel panel--contact">
    <p class="contact__intro">Outstanding Medicine,<br>Extraordinary Service. Located at</p>
    <p class="contact__address">418 Mill Brook Road, Bramfield, VT, across from the Bramfield Savings Bank.</p>
    <ul class="contact__lines">
      <li><svg viewBox="0 0 24 24"><path d="M6.6 10.8a15.1 15.1 0 0 0 6.6 6.6l2.2-2.2c.3-.3.7-.4 1-.2 1.1.4 2.3.6 3.6.6.6 0 1 .4 1 1V20c0 .6-.4 1-1 1C10.6 21 3 13.4 3 4c0-.6.4-1 1-1h3.5c.6 0 1 .4 1 1 0 1.3.2 2.5.6 3.6.1.3 0 .7-.2 1z"/></svg>802-555-0148</li>
      <li><svg viewBox="0 0 24 24"><path d="M6 3h12v5H6zM4 9h16a2 2 0 0 1 2 2v6h-4v4H6v-4H2v-6a2 2 0 0 1 2-2zm4 7v3h8v-3z"/></svg>802-555-0172</li>
      <li><svg viewBox="0 0 24 24"><path d="M2 5h20v14H2zm2 2v.5l8 5 8-5V7zm0 3v7h16v-7l-8 5z"/></svg>info@thecorvelpets.com</li>
    </ul>
    <h3 class="hours__title">HOSPITAL HOURS</h3>
    <ul class="hours__list">
      <li>Monday - 8:00am - 5:00pm</li>
      <li>Tuesday - 8am - 8:00pm</li>
      <li>Wednesday - 8am - 5:00pm</li>
      <li>Thursday - 8am - 6:00pm</li>
      <li>Friday - 8am - 4:00pm</li>
      <li>Saturday - 8am - 1:00pm</li>
      <li>Sunday - Closed</li>
    </ul>
    <div class="photo--dog" role="img" aria-label="Black and white photo of a happy dog with tongue out"></div>
    <div class="contact__marks">
      <p class="brand-name--small">Bramfield Animal Hospital</p>
      <div class="badge" aria-hidden="true"></div>
      <div class="badge badge--tall" aria-hidden="true"></div>
    </div>
  </section>

  <section class="panel panel--cover">
    <div class="cover__brand">
      <p class="brand-name">Bramfield<br>Animal Hospital</p>
      <span class="cover__brand-square" aria-hidden="true"></span>
    </div>
    <svg class="cover__hero" viewBox="0 0 280 280">
      <circle cx="150" cy="110" r="100" fill="none" stroke="var(--maroon)" stroke-width="6"/>
      <circle cx="150" cy="110" r="94" fill="#b9b2a8"/>
      <circle cx="66" cy="210" r="40" fill="#4a5a86" stroke="var(--navy)" stroke-width="5"/>
      <g role="img" aria-label="Group of dogs, a cat, a parrot and a snake; vet at work in small inset">
        <rect x="0" y="0" width="0" height="0"/>
      </g>
    </svg>
    <h1 class="cover__title">OUTSTANDING<br>MEDICINE<br>EXTRAORDINARY<br>SERVICE</h1>
    <svg class="cover__band" viewBox="0 0 360 70" preserveAspectRatio="none" aria-hidden="true">
      <polygon points="0,34 360,16 360,70 0,70" fill="var(--navy)"/>
      <polygon points="0,28 360,6 360,16 0,34" fill="var(--white)"/>
    </svg>
    <p class="cover__url" style="color: var(--white); bottom: 18px;">www.thecorvelpets.com</p>
  </section>

</main>
</body>
</html>
```